Suds Harbor Laundromat Wordpress Design

We need a Wordpress website design for our laundromat, Suds Harbor Atlanta, at www.sudsharboratlanta-example.com. We would like to have 6 pages: Home, About Us, Services, Locations, Reviews and Contact us. We will provide content for the text on each page. What we do: We are a full service laundromat that provides dry cleaning drop off, professional laundry services, wash dry fold and self service laundry to the local community. We would like to use the color scheme from our logo to convey a warm, safe, and bright business that caters to its diverse community.
Updates

I like the structure of this laundromat website: http://www.tumblewashhub-example.com/ Using my logo and color scheme in the above referenced website is what. Am looking for. The photos attached to the project with the female model should be used as a primary focus and supplemented by actual photos of the equipment.

Target Market(s)

Our target market is a diverse group of people from Midtown Atlanta - LGBTQ community /Locals/Regulars that have been coming to laundromat for 30 years.

Industry/Entity Type

Laundromat

Coding

Coded - Design and coding required

Number of Pages Required

5+ page

Font styles to use
Sans Serif

Colors
0054AA
0677BA
7BADD7
CADEEF
E8F1F8

Requirements
Must have
• Feature this video on the main page: https://video.example.com/Qx7mBr2Lp0Z

```html
<!DOCTYPE html>
<html lang="en">
<head>
<meta charset="utf-8">
<title>Suds Harbor Atlanta — Laundromat</title>
<link href="https://fonts.googleapis.com/css2?family=Open+Sans:wght@400;600;700&family=Lato:ital,wght@0,400;0,700;1,400&display=swap" rel="stylesheet">
<style>
:root{
  --brand-blue:#0054aa;
  --mid-blue:#0677ba;
  --wave-blue:#3d8fe0;
  --soft-blue:#cadeef;
  --pale-blue:#e8f1f8;
  --brand-red:#c8302e;
  --navy:#15234b;
  --ink:#22304a;
  --text:#555b66;
  --muted:#9aa0a8;
  --white:#ffffff;
}
*{box-sizing:border-box;margin:0;padding:0}
html,body{width:1200px;height:2849px;overflow:hidden;background:var(--white)}
body{font-family:'Open Sans',sans-serif;color:var(--ink);position:relative}
.abs{position:absolute}

/* header */
.site-header{position:absolute;left:0;top:0;width:1200px;height:70px;background:var(--white)}
.brand{position:absolute;left:157px;top:22px;font:700 22px/1 'Open Sans',sans-serif;color:var(--brand-red)}
.main-nav{position:absolute;top:30px;left:0;width:1200px;font:400 13px/1 'Open Sans',sans-serif;letter-spacing:.8px;color:#444}
.main-nav span{position:absolute;white-space:nowrap}

/* hero */
.hero-photo{position:absolute;left:0;top:70px;width:1200px;height:620px;
  background:linear-gradient(180deg,#a9c9c4 0%,#8fa7a6 30%,#6f7473 60%,#4c4b4a 100%)}
.hero-card{position:absolute;left:140px;top:290px;width:444px;height:252px;background:var(--brand-red);color:var(--white);padding:30px 0 0 28px}
.hero-card h1{font:400 40px/48px 'Open Sans',sans-serif;white-space:nowrap}
.hero-card p{font:400 13px/24px 'Lato',sans-serif;margin-top:16px;width:390px}
.hero-dots{position:absolute;left:158px;top:606px;display:flex;gap:6px;align-items:center}
.hero-dots i{display:block;width:7px;height:7px;border-radius:50%;background:rgba(255,255,255,.6)}
.hero-dots i.active{width:22px;border-radius:4px;background:var(--white)}

/* services */
.section-title{position:absolute;left:0;width:1200px;text-align:center;font:400 44px/1 'Open Sans',sans-serif;color:var(--ink)}
.service{position:absolute;top:867px;width:281px}
.service .shot{height:197px;background:linear-gradient(135deg,#c9cccc,#8e9393 60%,#6d7271)}
.service h3{font:600 27px/1 'Open Sans',sans-serif;margin-top:28px;color:var(--ink);white-space:nowrap}
.service p{font:400 13px/25.5px 'Lato',sans-serif;color:var(--text);margin-top:10px}

/* welcome */
.welcome{position:absolute;left:0;top:1310px;width:1200px;height:590px;background:var(--brand-blue)}
.video{position:absolute;left:101px;top:1420px;width:487px;height:334px;border-radius:4px;
  background:linear-gradient(135deg,#5b1a9e,#c21fc9 45%,#ff3fae 60%,#4a1d8c)}
.play{position:absolute;left:305px;top:1559px;width:56px;height:56px;border-radius:50%;background:var(--white);box-shadow:0 0 0 6px rgba(255,255,255,.25)}
.welcome-copy{position:absolute;left:636px;top:1412px;color:var(--white);width:440px}
.welcome-copy .kicker{font:400 34px/1.1 'Open Sans',sans-serif}
.welcome-copy h2{font:400 44px/1.1 'Open Sans',sans-serif}
.welcome-copy p{font:400 13px/24px 'Lato',sans-serif;margin-top:14px;width:420px}
.feature-list{list-style:none;margin-top:20px}
.feature-list li{position:relative;padding-left:42px;height:35.2px;font:600 13.5px/24px 'Open Sans',sans-serif;white-space:nowrap}
.feature-list li::before{content:"";position:absolute;left:0;top:0;width:26px;height:26px;border-radius:50%;background:rgba(255,255,255,.12)}
.feature-list li::after{content:"";position:absolute;left:9px;top:10px;width:6px;height:6px;border-top:1.5px solid var(--white);border-right:1.5px solid var(--white);transform:rotate(45deg)}

/* testimonials */
.quote-card{position:absolute;top:2075px;height:183px;background:var(--white);border:1px solid #eef0f3;text-align:center;font-family:'Lato',sans-serif;overflow:hidden}
.quote-card.main{left:307px;width:583px;box-shadow:0 6px 24px rgba(30,50,90,.08);border:none;padding:22px 50px}
.quote-card.side{width:240px;color:#b3b7bd;padding:22px 20px;opacity:.85}
.quote-card h4{font:400 15px/1 'Open Sans',sans-serif;color:var(--ink);white-space:nowrap}
.quote-card.side h4{color:#9aa0a8}
.quote-card p{font:italic 400 12.5px/25.5px 'Lato',sans-serif;color:#444a55;margin-top:12px}
.quote-card.side p{color:#b3b7bd}
.quote-mark{position:absolute;font:700 80px/1 Georgia,serif;color:#eceef1}
.slider-arrow{position:absolute;top:2156px;width:9px;height:9px;border-top:1.5px solid #555;border-right:1.5px solid #555}
.avatar{position:absolute;left:504px;top:2296px;width:48px;height:48px;border-radius:50%;background:linear-gradient(135deg,#e3c7a6,#b8835a)}
.reviewer{position:absolute;left:566px;top:2302px;font-family:'Open Sans',sans-serif}
.reviewer b{display:block;font:400 14px/1.3 'Open Sans',sans-serif;color:var(--mid-blue)}
.reviewer span{font:400 11px/1.3 'Open Sans',sans-serif;color:var(--brand-red)}

/* footer */
.footer-base{position:absolute;left:0;top:2470px;width:1200px;height:379px;background:var(--navy)}
.footer-col{position:absolute;top:2565px;color:var(--white);font-family:'Lato',sans-serif}
.footer-col h5{font:600 12px/1 'Open Sans',sans-serif;margin-bottom:30px}
.footer-col a{display:block;color:#d6dbe6;font:400 11.5px/27.3px 'Lato',sans-serif;text-decoration:none}
.footer-col address{font:normal 400 11.5px/19px 'Lato',sans-serif;color:#d6dbe6}
.contact-line{display:flex;align-items:center;gap:16px;margin-top:14px;font:400 11.5px/1 'Lato',sans-serif;color:#d6dbe6}
.contact-line i{width:20px;height:20px;border-radius:50%;background:rgba(255,255,255,.08);display:flex;align-items:center;justify-content:center}
.newsletter input{display:block;width:228px;height:38px;margin-top:14px;border:1px solid #3c4a72;background:transparent;color:var(--white);padding-left:14px;font:italic 400 11px 'Lato',sans-serif}
.newsletter input::placeholder{color:#6d7899}
.newsletter button{display:block;width:228px;height:37px;margin-top:12px;border:none;background:var(--brand-blue);color:var(--white);font:700 11px/1 'Open Sans',sans-serif;letter-spacing:1.5px}
.footer-rule{position:absolute;left:157px;top:2804px;width:888px;height:1px;background:#27355e}
.copyright{position:absolute;left:157px;top:2821px;font:400 10.5px/1 'Lato',sans-serif;color:var(--white)}
.copyright em{font-style:normal;color:var(--brand-red)}
.social{position:absolute;top:2815px;width:24px;height:24px;border-radius:50%;background:rgba(255,255,255,.08)}
</style>
</head>
<body>

<header class="site-header">
  <div class="brand">Suds Harbor</div>
  <nav class="main-nav">
    <span style="left:483px">HOME</span>
    <span style="left:555px">ABOUT US</span>
    <span style="left:656px">SERVICES</span>
    <span style="left:753px">LOCATIONS</span>
    <span style="left:864px">REVIEWS</span>
    <span style="left:963px">CONTACT US</span>
  </nav>
</header>

<div class="hero-photo" role="img" aria-label="Retro laundromat interior with rows of washers and a woman in a blue dress, shop name sign on the wall"></div>
<div class="hero-card">
  <h1>Professional laundry<br>service of Atlanta's</h1>
  <p>We are a full service laundromat that provides dry cleaning drop off, professional laundry services, wash dry fold and self service laundry to the local community.</p>
</div>
<svg class="abs" style="left:430px;top:541px" width="40" height="32" viewBox="0 0 40 32"><path d="M0 0H40L6 32Z" fill="#c8302e"/></svg>
<div class="hero-dots"><i></i><i class="active"></i><i></i><i></i></div>
<svg class="abs" style="left:0;top:640px" width="1200" height="80" viewBox="0 0 1200 80">
  <path d="M0 15 C250 65 450 62 620 38 C820 12 1000 12 1200 25 L1200 80 L0 80Z" fill="#3d8fe0"/>
  <path d="M0 30 C220 78 430 72 620 48 C820 22 1000 18 1200 28 L1200 80 L0 80Z" fill="#ffffff"/>
</svg>

<h2 class="section-title" style="top:785px">Services we offer</h2>

<article class="service" style="left:156px">
  <div class="shot" role="img" aria-label="Row of stainless front-load washers"></div>
  <h3>Dry Cleaning</h3>
  <p>Nam aliquam turpis sed interdum feugiat. Pellentesque habitant morbi tristique senectus et netus et malesuada fames ac turpis egestas. Pellentesque gravida convallis ante.</p>
</article>
<article class="service" style="left:460px">
  <div class="shot" role="img" aria-label="Open top-load coin washers"></div>
  <h3>Coin Laundry</h3>
  <p>Donec et efficitur ipsum, quis laoreet sapien. Suspendisse dignissim nibh vitae enim aliquet congue. Ut a cursus est. Nunc pharetra eu lacus at hendrerit imperdiet lobortis vulputate..</p>
</article>
<article class="service" style="left:764px">
  <div class="shot" role="img" aria-label="Laundromat aisle lined with large washers"></div>
  <h3>Professional Laundry</h3>
  <p>Suspendisse dignissim nibh vitae enim aliquet congue. Ut a cursus est. Nunc pharetra eu lacus at hendrerit. Integer imperdiet lobortis vulputate. Pellentesque interdum egestas.</p>
</article>

<section class="welcome"></section>
<svg class="abs" style="left:0;top:1840px" width="1200" height="70" viewBox="0 0 1200 70">
  <path d="M0 48 C300 20 500 12 700 15 C900 18 1050 25 1200 50 L1200 70 L0 70Z" fill="#ffffff"/>
</svg>
<div class="video" role="img" aria-label="Promotional video still: a dancer in a neon-lit laundromat"></div>
<div class="play"></div>
<svg class="abs" style="left:326px;top:1578px" width="16" height="18" viewBox="0 0 16 18"><path d="M1 1L15 9L1 17Z" fill="#0054aa"/></svg>
<div class="welcome-copy">
  <div class="kicker">Welcome to</div>
  <h2>Suds Harbor</h2>
  <p>Class aptent taciti sociosqu ad litora torquent per conubia nostra, per inceptos himenaeos. Etiam iaculis semper vestibulum. Nunc luctus, ligula ut eleifend blandit, leo turpis viverra nisl</p>
  <ul class="feature-list">
    <li>In Business over 45 years</li>
    <li>Voted "BEST COIN LAUNDRY" - Multiple years</li>
    <li>One of Atlanta's First, Finest, &amp; Friendliest Coin Laundries</li>
    <li>The best Wash-Dry-Fold in town</li>
    <li>Over 50 well maintained machines</li>
  </ul>
</div>

<h2 class="section-title" style="top:1980px">Our happy customers</h2>

<div class="quote-card side" style="left:-1px;text-align:left;padding-left:0">
  <h4 style="margin-left:-4px">act to &nbsp;it that matters”</h4>
  <p>es and others that it's common to get a series of disappointments. Like many . But often, instead of a 400 page book you sometimes...</p>
</div>
<div class="quote-card side" style="left:963px;text-align:left;padding-left:70px">
  <h4>“Its not what I</h4>
  <p>Unexpected challenges affec stuck in a routine of destructi others, we've found help in bo or a 30</p>
</div>
<div class="abs" style="left:0;top:2306px;font:400 10px 'Open Sans',sans-serif;color:#c8cbd0">nia</div>

<div class="quote-card main">
  <span class="quote-mark" style="left:28px;top:30px">“</span>
  <span class="quote-mark" style="right:230px;top:118px">”</span>
  <h4 style="position:relative">“Sed dignissim eu enim vitae dictum. Fusce mi ultricies a magna”</h4>
  <p style="position:relative">Class aptent taciti sociosqu ad litora torquent per conubia nostra, per inceptos himenaeos. Etiam iaculis semper vestibulum. Nunc luctus, ligula ut eleifend blandit, leo turpis viverra nisl, ut vulputate quam urna vitae tellus. Praesent sem odio, convallis at lectus eget, mollis porta arcu...</p>
</div>
<svg class="abs" style="left:585px;top:2257px" width="26" height="14" viewBox="0 0 26 14"><path d="M0 0H26L13 14Z" fill="#ffffff"/></svg>
<span class="slider-arrow" style="left:273px;transform:rotate(-135deg)"></span>
<span class="slider-arrow" style="left:916px;transform:rotate(45deg)"></span>
<div class="avatar" role="img" aria-label="Reviewer portrait"></div>
<div class="reviewer"><b>Marla Quinn</b><span>Portland, Oregon</span></div>

<svg class="abs" style="left:0;top:2395px" width="1200" height="90" viewBox="0 0 1200 90">
  <path d="M0 10 C250 60 450 70 650 55 C850 40 1000 25 1200 35 L1200 90 L0 90Z" fill="#c8302e"/>
  <path d="M0 32 C250 78 450 80 650 68 C850 55 1000 42 1200 48 L1200 90 L0 90Z" fill="#15234b"/>
</svg>
<footer class="footer-base"></footer>

<div class="footer-col" style="left:157px">
  <h5>Contact Info</h5>
  <address>2810 Harbor Loop NE., # 112,<br>Atlanta, GA 30399</address>
  <div class="contact-line" style="margin-top:18px"><i><svg width="9" height="7" viewBox="0 0 9 7"><rect x=".5" y=".5" width="8" height="6" fill="none" stroke="#d6dbe6"/><path d="M.5 .5L4.5 4L8.5 .5" fill="none" stroke="#d6dbe6"/></svg></i>hello@sudsharbor-example.com</div>
  <div class="contact-line"><i><svg width="9" height="9" viewBox="0 0 9 9"><path d="M1 1.5C1 5 4 8 7.5 8L8 6.5L6 5.5L5 6.5C4 6 3 5 2.5 4L3.5 3L2.5 1Z" fill="#d6dbe6"/></svg></i>+ (555) 014-2290</div>
</div>
<div class="footer-col" style="left:459px">
  <h5>About</h5>
  <a>About us</a><a>Services</a><a>Locations</a><a>Review</a><a>Contact us</a>
</div>
<div class="footer-col" style="left:641px">
  <h5>More</h5>
  <a>Terms and conditions</a><a>Privacy policy</a><a>Sitemap</a><a>Contact</a>
</div>
<div class="footer-col newsletter" style="left:815px">
  <h5 style="margin-bottom:22px">Newsletters</h5>
  <div style="font:400 11.5px 'Lato',sans-serif;color:#d6dbe6">Signup below to join our maling list</div>
  <input type="email" placeholder="Email address">
  <button type="button">SUBSCRIBE NOW</button>
</div>

<div class="footer-rule"></div>
<div class="copyright">© 2021 <em>Suds Harbor Atlanta</em> . All rights reserved</div>
<span class="social" style="left:911px"></span>
<span class="social" style="left:945px"></span>
<span class="social" style="left:981px"></span>
<span class="social" style="left:1017px"></span>

</body>
</html>
```